Food label for BarBQ sauce and creole seasoning under the name HONEY BAYOU

I need a label design using the name "HONEY BAYOU" that will be used on bottles of Bar B Q sauce, both Creole and Cajun, and dry Cajun and dry Creole seasoning. I have attached a copy of the letter style we will be using. It is NOT a religious product or has any religious meaning. It comes from a saying old southerners used when they tasted something special -"Oh Honey Bayou". The labels for the Bar B Q sauces will be 5" wide by 3" tall, and the dry seasonings will be 5" wide by 3 1/2" tall. The products will that they are from South Louisiana and should reflect the typical food from the New Orleans area. This produce name is a REGISTERED TRADE NAME with the US trademark office.

```html
<!DOCTYPE html>
<html lang="en">
<head>
<meta charset="utf-8">
<title>Honey Bayou – Creole Bar B Q and Dipping Sauce Label</title>
<link rel="stylesheet" href="https://fonts.googleapis.com/css2?family=Almendra:wght@700&family=Chewy&display=swap">
<style>
  :root {
    --backdrop: #e8733a;
    --backdrop-edge: #b8451f;
    --label-red: #d41f26;
    --label-red-bright: #e3232b;
    --band-black: #1c1010;
    --sauce-dark: #3e1a14;
    --sauce-deep: #a51c22;
    --cloud-white: #ffffff;
    --script-red: #d81e27;
    --name-white: #ffffff;
  }
  * { box-sizing: border-box; margin: 0; padding: 0; }
  html, body {
    width: 1200px;
    height: 800px;
    overflow: hidden;
  }
  body {
    background: radial-gradient(ellipse at center, var(--backdrop) 0%, var(--backdrop-edge) 100%);
    position: relative;
  }
  .label {
    position: absolute;
    left: 150px;
    top: 85px;
    width: 900px;
    height: 630px;
    background: linear-gradient(180deg, var(--sauce-dark) 0%, var(--sauce-deep) 100%);
    box-shadow: 0 14px 30px rgba(60, 20, 5, 0.35);
    overflow: hidden;
  }
  .label__header {
    position: absolute;
    left: 0;
    top: 0;
    width: 100%;
    height: 210px;
    background: var(--label-red);
    border-top: 8px solid var(--label-red-bright);
  }
  .label__header-stripe {
    height: 16px;
    background: var(--band-black);
  }
  .brand-name {
    font-family: "Almendra", Georgia, serif;
    font-weight: 700;
    color: var(--name-white);
    font-size: 70px;
    line-height: 80px;
    letter-spacing: 2px;
    text-align: center;
    margin-top: 12px;
  }
  .flavour-cloud {
    position: absolute;
    left: 135px;
    top: 232px;
    width: 630px;
    height: 350px;
  }
  .flavour-cloud svg {
    position: absolute;
    inset: 0;
    width: 100%;
    height: 100%;
    overflow: visible;
    filter: drop-shadow(0 6px 8px rgba(0, 0, 0, 0.35));
  }
  .flavour-cloud__shape { fill: var(--cloud-white); }
  .flavour-cloud__stitch {
    fill: none;
    stroke: var(--script-red);
    stroke-width: 3;
    stroke-dasharray: 1 8;
    stroke-linecap: round;
  }
  .product-name {
    font-family: "Chewy", "Comic Sans MS", cursive;
    font-size: 58px;
    fill: var(--script-red);
  }
</style>
</head>
<body>
  <section class="label" aria-label="Honey Bayou sauce label">
    <header class="label__header">
      <div class="label__header-stripe"></div>
      <h1 class="brand-name">HONEY<br>BAYOU</h1>
    </header>
    <div class="flavour-cloud">
      <svg viewBox="0 0 630 350" role="group" aria-label="Creole Bar B Q and Dipping Sauce">
        <path class="flavour-cloud__shape" d="M 90 90 A 60 60 0 0 1 200 50 A 70 70 0 0 1 320 30 A 70 70 0 0 1 440 45 A 60 60 0 0 1 550 95 A 55 55 0 0 1 600 190 A 60 60 0 0 1 545 285 A 60 60 0 0 1 440 320 A 70 70 0 0 1 320 330 A 70 70 0 0 1 195 315 A 60 60 0 0 1 85 280 A 55 55 0 0 1 35 185 A 55 55 0 0 1 90 90 Z"/>
        <path class="flavour-cloud__stitch" transform="translate(317 180) scale(0.94) translate(-317 -180)" d="M 90 90 A 60 60 0 0 1 200 50 A 70 70 0 0 1 320 30 A 70 70 0 0 1 440 45 A 60 60 0 0 1 550 95 A 55 55 0 0 1 600 190 A 60 60 0 0 1 545 285 A 60 60 0 0 1 440 320 A 70 70 0 0 1 320 330 A 70 70 0 0 1 195 315 A 60 60 0 0 1 85 280 A 55 55 0 0 1 35 185 A 55 55 0 0 1 90 90 Z"/>
        <g class="product-name" text-anchor="middle">
          <text x="317" y="128" textLength="240" lengthAdjust="spacingAndGlyphs">CREOLE</text>
          <text x="317" y="195" textLength="350" lengthAdjust="spacingAndGlyphs">BAR B Q AND</text>
          <text x="317" y="262" textLength="400" lengthAdjust="spacingAndGlyphs">DIPPING SAUCE</text>
        </g>
      </svg>
    </div>
  </section>
</body>
</html>
```